Tuition Center Website

We need a new web site for a tutoring company based in sydney.

We only teach senior highschool students and pride ourselves on building the students abilities to think their way through life.

I would like a bright and vibrant website that looks professional and modern.
It needs to look simple and neat but also have the functionality we need.
Images and flash would be good.

Please keep in mind that the site must be appealing to a younger audience.

We need a multipage website with the following navigation bars:

1.Home (As logo not "home" button)
I would like a news box/ticker somewhere that can stream our chatterbook and flitter feeds and also any news updates we want to put up.
Subscribe to newsletter button.

2. About us.
This needs to be a pull down into:
-What we do
-Why we do it
-How we do it

3. Courses
Pulldown into:
-Maths
-English
-Science
(we may need to attach extra pages behind these e.g. Courses/Science/Physics or Courses/Science/Chemistry and possibly add a link to a new quizzo form)

4. Inspired
This page is like a blog page where we can upload videos, links to articles that we find to be inspiring and hopefully will inspire others.

5. Inspire
This is a recruitment page. Only content here.

6. Contact us.
Mapzy map widget and a 'contact us' form

* Our branding requires green close to #12FF3D

***Please have a look at the current website.
@ www.brindlelearning.com.au

Thanks everybody hope the revision of my brief is better and more informative than my last one

Target Market(s)

senior highschool students aged 15-19, parents ( to a lesser degree)

Industry/Entity Type

It Company

Requirements
Must have
• Ability to change content on pages.

The green doesn't have to be everywhere, but it must be obvious that it is our colour.

Nice to have
• Sites with a nicer mix of images and flash will be given more consideration. But then again, if you amaze us, you amaze us and we will go with your design.
Should not have
• Should stay away from ocre, brown colours and serif fonts.

```html
<!DOCTYPE html>
<html lang="en">
<head>
<meta charset="utf-8">
<title>Brindle Learning – HSC coaching &amp; mentoring</title>
<link href="https://fonts.googleapis.com/css2?family=Archivo+Narrow:wght@400;500;600&family=Arimo:wght@400;700&family=Open+Sans:ital,wght@0,400;0,600;1,400&family=Kaushan+Script&display=swap" rel="stylesheet">
<style>
:root{
  --green-dark:#3b7a1f;
  --green-mid:#5fa52b;
  --green-light:#b5dc55;
  --brand-green:#12c83a;
  --yellow-top:#ffd21c;
  --yellow-bottom:#f7a600;
  --page-bg:#efefef;
  --card-border:#dcdcdc;
  --text-dark:#4a4a4a;
  --text-muted:#a3a3a3;
  --link-blue:#3b5998;
  --button-blue:#2aa8e0;
  --footer-bg:#0b0b0b;
  --white:#ffffff;
}
*{margin:0;padding:0;box-sizing:border-box}
html,body{width:849px;height:1200px;overflow:hidden}
body{position:relative;background:var(--page-bg);font-family:"Open Sans",Arial,sans-serif;color:var(--text-dark)}
.abs{position:absolute}

/* header */
.site-header{left:0;top:0;width:849px;height:127px;background:linear-gradient(#3f7f20,#4a8d26)}
.brand{left:80px;top:10px;width:90px}
.brand-square{width:77px;height:66px;background:var(--white)}
.brand-name{margin-top:4px;color:var(--white);font-weight:600;font-size:16px;line-height:15px;text-align:center;width:86px}
.brand-url{color:var(--white);font-size:6px;margin-top:2px;width:96px;text-align:center}
.tagline{left:188px;top:48px;color:var(--white);font-family:"Kaushan Script",cursive;font-size:24px;letter-spacing:0.5px;white-space:nowrap}
.main-nav{top:93px;left:0;height:20px}
.main-nav a{position:absolute;top:0;height:20px;line-height:20px;color:var(--white);font-family:Arimo,Arial,sans-serif;font-weight:700;font-size:10px;text-decoration:none;white-space:nowrap}
.main-nav a.current{background:linear-gradient(var(--yellow-top),var(--yellow-bottom));padding:0 9px}

/* hero */
.hero{left:0;top:127px;width:849px;height:370px;background:radial-gradient(ellipse 520px 300px at 424px 150px,#c4e46a 0%,#8cc43e 55%,#4f9226 100%);clip-path:ellipse(900px 370px at 424px 0)}
.hero-title{left:0;top:140px;width:849px;text-align:center;color:var(--white);font-family:"Archivo Narrow",Arial,sans-serif;font-size:64px;line-height:72px;font-weight:400}
.hero-sub{left:0;top:206px;width:849px;text-align:center;color:var(--white);font-family:"Archivo Narrow",Arial,sans-serif;font-size:22px;font-weight:400}
.btn{display:block;text-align:center;color:var(--white);font-family:"Archivo Narrow",Arial,sans-serif;font-weight:600;text-decoration:none;box-shadow:0 6px 8px -4px rgba(0,0,0,.35)}
.btn-yellow{background:linear-gradient(var(--yellow-top),var(--yellow-bottom))}
.btn-green{background:linear-gradient(#b9e34a,#63b31d)}
.btn-hero{top:243px;width:127px;height:34px;line-height:34px;font-size:17px}

.screen{background:linear-gradient(#d9d9d9,#b7b7b7);border-radius:6px;box-shadow:0 8px 18px rgba(0,0,0,.25)}
.screen-photo{position:absolute;background:linear-gradient(135deg,#7c9a52,#a58566 55%,#5a6b3e)}

/* cards */
.card{background:var(--white);border:1px solid var(--card-border)}
.icon-slot{border-radius:8px}
.card-title{font-family:"Archivo Narrow",Arial,sans-serif;font-size:18px;line-height:22px;font-weight:400;color:var(--text-dark)}
.card-copy{font-style:italic;font-size:10.5px;line-height:17px;color:var(--text-muted);text-align:center}
.card-author{font-weight:600;font-size:10.5px;color:#8a8a8a;text-align:center}
.btn-card{top:830px;width:127px;height:32px;line-height:32px;font-size:17px}

.address-head{left:550px;top:665px;width:224px;height:40px;line-height:40px;text-align:center;color:var(--white);font-family:"Archivo Narrow",Arial,sans-serif;font-size:24px;background:linear-gradient(#c1e84e,#6fbb1f);box-shadow:0 5px 6px -4px rgba(0,0,0,.3)}

/* updates */
.updates-title{left:173px;top:912px;font-family:"Archivo Narrow",Arial,sans-serif;font-size:28px;font-weight:400;color:var(--text-dark)}
.post-title{font-family:"Archivo Narrow",Arial,sans-serif;font-size:13px;font-weight:400;color:var(--text-dark)}
.post-copy{font-style:italic;font-size:10px;line-height:17px;color:var(--text-muted);width:425px}
.read-more{display:inline-block;background:var(--button-blue);color:var(--white);font-style:normal;font-size:6px;font-weight:600;padding:2px 4px;margin-left:5px;vertical-align:middle}
.divider{left:93px;width:415px;border-top:1px dashed #d6d6d6}

/* social widget */
.social-name{font-size:10.5px;line-height:12px;color:var(--link-blue);font-weight:600}
.social-small{font-size:8px;color:#333}
.social-small a{color:var(--link-blue);text-decoration:none}
.fan-photo{width:36px;height:36px;background:linear-gradient(#d8b39a,#8a6a55);border:1px solid #ddd}
.fan-name{width:44px;text-align:center;font-size:7.5px;color:#555}

.site-footer{left:0;top:1162px;width:849px;height:38px;background:var(--footer-bg);color:var(--white);font-size:8.5px;padding:17px 0 0 72px}
</style>
</head>
<body>

<header class="site-header abs">
  <div class="brand abs">
    <div class="brand-square"></div>
    <div class="brand-name">brindle learning</div>
    <div class="brand-url">www.brindlelearning.com.au</div>
  </div>
  <p class="tagline abs">inspiring minds.nurturing potentential.equipping succes</p>
  <nav class="main-nav abs">
    <a href="#" style="left:459px">ABOUT US</a>
    <a href="#" style="left:529px">COURSES</a>
    <a href="#" class="current" style="left:587px">INSPIRED</a>
    <a href="#" style="left:665px">INSPIRE</a>
    <a href="#" style="left:719px">CONTACT US</a>
  </nav>
</header>

<section class="hero abs"></section>
<h1 class="hero-title abs">i am brindle.</h1>
<p class="hero-sub abs">&nbsp;&nbsp;&nbsp;&nbsp;real HSC coaching &amp; mentoring.</p>
<a href="#" class="btn btn-yellow btn-hero abs" style="left:294px">ENQUIRE NOW</a>
<a href="#" class="btn btn-green btn-hero abs" style="left:432px">TAKE A TOUR</a>

<div class="screen abs" style="left:75px;top:340px;width:168px;height:240px" role="img" aria-label="Display showing a tutor helping a student at a desk">
  <div class="screen-photo" style="left:12px;top:14px;width:150px;height:160px"></div>
</div>
<div class="screen abs" style="left:605px;top:340px;width:168px;height:240px" role="img" aria-label="Display showing a smiling group of students">
  <div class="screen-photo" style="left:6px;top:14px;width:150px;height:160px"></div>
</div>
<div class="screen abs" style="left:238px;top:302px;width:369px;height:306px" role="img" aria-label="Large display showing students talking together outdoors at a picnic table">
  <div class="screen-photo" style="left:16px;top:16px;width:337px;height:202px"></div>
</div>

<article class="card abs" style="left:73px;top:665px;width:224px;height:183px">
  <div class="icon-slot abs" style="left:18px;top:-8px;width:76px;height:66px;background:linear-gradient(#5fb4ea,#46b03c)" role="img" aria-label="Speech bubbles icon"></div>
  <h2 class="card-title abs" style="left:108px;top:16px">What Our<br>Students Say</h2>
  <p class="card-copy abs" style="left:20px;top:70px;width:184px">"Curabitur euismod justo vitae massa sagittis dictum. Quisque ut nulla leo."</p>
  <p class="card-author abs" style="left:20px;top:112px;width:184px">Tom REYES - Student</p>
</article>
<a href="#" class="btn btn-yellow btn-card abs" style="left:123px">LEARN MORE</a>

<article class="card abs" style="left:311px;top:665px;width:224px;height:183px">
  <div class="icon-slot abs" style="left:18px;top:-6px;width:66px;height:66px;background:linear-gradient(#f6d04a,#e9a61e)" role="img" aria-label="Address book icon"></div>
  <h2 class="card-title abs" style="left:94px;top:16px">Your FREE Trial<br>Lesson</h2>
  <p class="card-copy abs" style="left:20px;top:70px;width:184px">Vestibulum feugiat magna in mi tincid-unt a blandit dui mollis. Curabitur euis-mod justo vitae massa sagittis dictum. Quisque ut nulla leo.</p>
</article>
<a href="#" class="btn btn-yellow btn-card abs" style="left:359px">LEARN MORE</a>

<article class="card abs" style="left:550px;top:665px;width:224px;height:183px">
  <div class="abs" style="left:0;top:40px;width:222px;height:142px;background:linear-gradient(135deg,#e9e4d4,#d9d2bf)" role="img" aria-label="Street map of the centre's location"></div>
</article>
<div class="address-head abs">Our Address</div>
<a href="#" class="btn btn-green btn-card abs" style="left:604px">Contact us</a>

<section class="card abs" style="left:73px;top:895px;width:462px;height:242px"></section>
<div class="icon-slot abs" style="left:92px;top:890px;width:68px;height:58px;background:linear-gradient(#e6c9a0,#c79a67)" role="img" aria-label="Notepad and pencil icon"></div>
<h2 class="updates-title abs">Our Latest Updates</h2>
<h3 class="post-title abs" style="left:93px;top:963px">Native Advertising</h3>
<p class="post-copy abs" style="left:93px;top:985px">Vestibulum feugiat magna in mi tincidunt a blandit dui mollis. Curabitur euismod justo vitae massa sagittis dictum. Quisque ut nulla leo.<span class="read-more">READ MORE</span></p>
<div class="divider abs" style="top:1035px"></div>
<h3 class="post-title abs" style="left:93px;top:1049px">Teething Pains</h3>
<p class="post-copy abs" style="left:93px;top:1071px">Vestibulum feugiat magna in mi tincidunt a blandit dui mollis. Curabitur euismod justo vitae massa sagittis dictum. Quisque ut nulla leo.<span class="read-more">READ MORE</span></p>

<aside class="card abs" style="left:553px;top:898px;width:217px;height:239px">
  <div class="fan-photo abs" style="left:11px;top:11px;width:28px;height:28px" role="img" aria-label="Page profile photo"></div>
  <p class="social-name abs" style="left:48px;top:10px">Brindle Learning<br>Here <span style="font-weight:400;font-size:9px">on chatterbook</span></p>
  <p class="social-small abs" style="left:48px;top:53px">You like this. <a href="#">Unlike</a></p>
  <div class="abs" style="left:8px;top:70px;width:176px;border-top:1px solid #e5e5e5"></div>
  <p class="social-small abs" style="left:10px;top:78px">5,000 people like <a href="#">Brindle Learning</a></p>
  <div class="fan-photo abs" style="left:11px;top:104px" role="img" aria-label="Fan photo"></div>
  <div class="fan-photo abs" style="left:54px;top:104px" role="img" aria-label="Fan photo"></div>
  <div class="fan-photo abs" style="left:97px;top:104px" role="img" aria-label="Fan photo"></div>
  <div class="fan-photo abs" style="left:140px;top:104px" role="img" aria-label="Fan photo"></div>
  <p class="fan-name abs" style="left:7px;top:144px">Pip</p>
  <p class="fan-name abs" style="left:50px;top:144px">Juno</p>
  <p class="fan-name abs" style="left:93px;top:144px">Figs</p>
  <p class="fan-name abs" style="left:136px;top:144px">Plums</p>
  <div class="fan-photo abs" style="left:11px;top:162px" role="img" aria-label="Fan photo"></div>
  <div class="fan-photo abs" style="left:54px;top:162px" role="img" aria-label="Fan photo"></div>
  <div class="fan-photo abs" style="left:97px;top:162px" role="img" aria-label="Fan photo"></div>
  <div class="fan-photo abs" style="left:140px;top:162px" role="img" aria-label="Fan photo"></div>
  <p class="fan-name abs" style="left:7px;top:202px">Milo</p>
  <p class="fan-name abs" style="left:50px;top:202px">Dex</p>
  <p class="fan-name abs" style="left:93px;top:202px">Ana</p>
  <p class="fan-name abs" style="left:136px;top:202px">Rory</p>
  <div class="abs" style="left:8px;top:218px;width:176px;border-top:1px solid #e5e5e5"></div>
  <p class="social-small abs" style="left:9px;top:222px"><span style="display:inline-block;width:9px;height:9px;background:var(--link-blue);vertical-align:middle"></span> chatterbook social plugin</p>
</aside>

<footer class="site-footer abs">© 2013 brindle learning | HSC tutoring &amp; mentoring</footer>

</body>
</html>
```